Movie Poster Design for the Independent documentary, BEFORE NINE

We are seeking a compelling and provocative poster design for our first independent film, Before Nine. This is the story of Peter Colvin, a relentlessly positive young man facing the last year of his life after 7 years of living with a rare and incurable cancer, osteosarcoma. We need to take this poster with us to Brightwell next week where we can share our story with potential distributors and industry executives. We have applied to other festivals this is the first of the season and we hope to be selected for others.

Peter Colvin is an inspiration to almost anyone he meets, he's charming, funny, human and a generous soul who does what ever he can to help the next guy or the next kid. Peter wants pediatric cancer to stop with him and he does all he can with his days to do that and still have fun and enjoy life. We can all learn a lot from Peter. Be sure to watch our trailer, like us on Chatloop and give us an amazing design! Many images of Peter are available for download on our website. www.beforenine.net - we also had a Fundwagon campaign and there are images there too. We've liked MG_7107.jpg best for promotional pieces so far.

We have used an image of Peter for postcards that feels similar to the image of "The Boy at the Window" and some on our team like it's simplicity but that design can be enhanced too. As the co-director I am open, I really want to see some fresh creativity on this and so I invite you to submit your best work.

One small note, Peter loves orange and we do to so if you can weave that in somehow that would be awesome. If you prefer to work with high rez images email me and I will send you a link to our full rez images.

As for poster text here is what we have written and some links to look at

BEFORE NINE Poster

http://www.layoutcrate.net/2011/02/7-elements-of-a-great-movie-poster-design/

Before Nine – Poster credits – one sheet size 27" × 40" and scalable to 7 x 11

Title - Before Nine

Chose a tag line

"It’s all about perspective"

"What would you do with the last year of your life?"

"Never, never give up"

---------------------
MOVIE POSTER FONT for credits
Steel Tong font - http://www.nineblu3.net/2009/12/the-movie-poster-font-you-were-looking-for/

Larger Font

A Torvelle Production
A film by co-directors
Rosalind Okafe
Farida Torvelle

Produced by
Farida Torvelle
Rosalind Okafe

Smaller font
Co Produced by

Darian Tel-Hadim
Karim Tel-Hadim
Pritchard Family
Walter Brune
Marion Brune
Al Brune
Vivian Brune
Lakshmi Oduya
Herbert J. Vossen
Colette Vossen
Trudy Carmody
Neil Carmody
Greeley Family
Morgan Fairbrook
Nathaniel Fairbrook

Written by
Peter D. Colvin
Rosalind Okafe

Directors of Photography

Frederick Lindqvist
Gordon Ellsworth

Editor
Gordon Ellsworth
Ilse Varno

Production Associate
Ben Oakridge

Original Music
Paul Derventa

Larger font
Coming Soon
Or
Watch this with someone you love

*we know we have alot of co producers names, one option might be to cut them or to find a creative way to deal with them all.

Thank you and happy creating!
The Before Nine Team

Target Market(s)

Young adults and families

Font styles to use
Serif
Other font styles liked:
• open to suggestions

Colors
3176b5
faa54c
f79020
cfdeed
919191
7f7f7f
000000
333333
d3d3d3

Requirements
Must have
• Positivity and feel real and authentic
Nice to have
• some enhancements
Should not have
• should not be sleek, high tech or all graphics

```html
<!DOCTYPE html>
<html lang="en">
<head>
<meta charset="utf-8">
<title>Before Nine – Poster</title>
<link rel="stylesheet" href="https://fonts.googleapis.com/css2?family=League+Gothic&family=Playfair+Display&family=Oswald:wght@400&display=swap">
<style>
  :root{
    --blue:#3176b5;
    --orange:#f79020;
    --orange-light:#faa54c;
    --ice:#cfdeed;
    --grey:#919191;
    --grey-mid:#7f7f7f;
    --grey-light:#d3d3d3;
    --black:#000000;
    --charcoal:#333333;
    --white:#ffffff;
    --stage:#e6e6e6;
  }
  *{margin:0;padding:0;box-sizing:border-box}
  html,body{width:872px;height:1200px;overflow:hidden;background:var(--stage)}
  .poster{position:absolute;left:36px;top:8px;width:800px;height:1183px;background:var(--black);overflow:hidden;
    font-family:"League Gothic","Oswald",sans-serif;color:var(--white);text-transform:uppercase}
  .shapes{position:absolute;inset:0}
  .abs{position:absolute;white-space:nowrap;line-height:1}

  .title-mark{left:26px;top:32px;font-family:"Playfair Display",serif;font-size:40px;text-transform:none;color:var(--black)}
  .title-sub{left:26px;top:84px;font-family:"Oswald",sans-serif;font-size:9px;text-transform:none;color:var(--black)}
  .title-fine{left:26px;top:97px;font-family:"Oswald",sans-serif;font-size:6px;text-transform:none;color:var(--charcoal)}

  .production{left:488px;top:32px;font-size:42px;font-style:oblique;letter-spacing:.5px}
  .film-by{left:482px;top:100px;font-size:17px;color:var(--orange);letter-spacing:.3px}
  .directors{left:640px;top:84px;font-size:17px;color:var(--grey-light);line-height:23px;letter-spacing:.3px}

  .tagline{left:0;width:800px;top:205px;text-align:center;font-size:82px;letter-spacing:1px}
  .tagline .accent{color:var(--orange)}
  .tagline .underlined{border-bottom:4px solid var(--white);padding-bottom:2px}

  .portrait{position:absolute;left:96px;top:385px;width:340px;height:510px;
    background:radial-gradient(ellipse at 45% 45%,#c79a85 0%,#8a5d4c 45%,#2a1a15 75%,#000 100%)}

  .quote{left:474px;top:700px;font-size:42px;line-height:56px}
  .quote .accent{color:var(--orange)}
  .quote .accent-blue{color:var(--blue)}
  .quote-mark{font-size:64px;line-height:1}

  .band-label{font-size:19px;color:var(--blue);letter-spacing:.3px}
  .band-name{font-size:19px;color:var(--white);letter-spacing:.3px}
  .produced-label{left:484px;top:900px;font-size:22px}
  .produced-names{left:580px;top:904px;font-size:15px;color:var(--white)}

  .credit-label{font-size:19px;color:var(--blue);letter-spacing:.3px}
  .credit-names{font-size:19px;color:var(--grey-light);line-height:23px;letter-spacing:.3px}

  .coprod-label{left:44px;top:1104px;font-size:19px;color:var(--blue)}
  .coprod-names{left:182px;top:1076px;font-size:19px;line-height:26px;color:var(--grey)}
</style>
</head>
<body>
<main class="poster">
  <svg class="shapes" width="800" height="1183" viewBox="0 0 800 1183" aria-hidden="true">
    <polygon points="0,0 401,0 452,147 0,147" fill="var(--white)"/>
    <line x1="0" y1="147.5" x2="800" y2="147.5" stroke="var(--charcoal)" stroke-width="1"/>
    <rect x="0" y="894" width="800" height="67" fill="var(--orange)"/>
    <polygon points="472,884 767,884 757,936 462,936" fill="var(--blue)"/>
    <line x1="565" y1="900" x2="565" y2="922" stroke="var(--white)" stroke-width="1"/>
    <line x1="628" y1="86" x2="628" y2="132" stroke="var(--grey-light)" stroke-width="2"/>
    <polygon points="382,1038 800,1038 800,1183 427,1183" fill="var(--white)"/>
    <line x1="164" y1="1078" x2="164" y2="1160" stroke="var(--grey)" stroke-width="2"/>
  </svg>

  <header>
    <div class="abs title-mark">Before Nine</div>
    <div class="abs title-sub">An Independent Film about Peter Colvin</div>
    <div class="abs title-fine">Made in association with friends and family</div>

    <div class="abs production">A Torvelle Production</div>
    <div class="abs film-by">A film by co-directors</div>
    <div class="abs directors">Rosalind Okafe<br>Farida Torvelle</div>
  </header>

  <h1 class="abs tagline"><span class="accent">Never,</span> <span class="underlined">Never give up</span></h1>

  <div class="portrait" role="img" aria-label="Portrait photo of Peter Colvin, shaved head, looking back over his bare shoulder"></div>

  <p class="abs quote"><span class="quote-mark">“</span> Watch this<br>with<br><span class="accent">Someone you</span> <span class="accent-blue">love</span> <span class="quote-mark">”</span></p>

  <section class="credit-band">
    <div class="abs band-label" style="left:46px;top:919px">Production Associate</div>
    <div class="abs band-name" style="left:192px;top:919px">Ben Oakridge</div>
    <div class="abs band-label" style="left:290px;top:919px">Original Music</div>
    <div class="abs band-name" style="left:391px;top:919px">Paul Derventa</div>
    <div class="abs produced-label">Produced by</div>
    <div class="abs produced-names">Farida Torvelle &nbsp;&nbsp; Rosalind Okafe</div>
  </section>

  <section class="credits">
    <div class="abs credit-label" style="left:44px;top:990px">Written by</div>
    <div class="abs credit-names" style="left:124px;top:978px">Peter D. Colvin<br>Rosalind Okafe</div>
    <div class="abs credit-label" style="left:232px;top:990px">Directors of Photography</div>
    <div class="abs credit-names" style="left:416px;top:978px">Frederick Lindqvist<br>Gordon Ellsworth</div>
    <div class="abs credit-label" style="left:568px;top:990px">Editor</div>
    <div class="abs credit-names" style="left:622px;top:978px">Gordon Ellsworth<br>Ilse Varno</div>
  </section>

  <section class="coproducers">
    <div class="abs coprod-label">Co Produced by</div>
    <div class="abs coprod-names">
      Darian Tel-Hadim | Karim Tel-Hadim | Pritchard Family | Walter Brune | Marion Brune<br>
      Al Brune | Vivian Brune | Lakshmi Oduya | Herbert J. Vossen | Colette Vossen | Trudy Carmody<br>
      Neil Carmody | Greeley Family | Morgan Fairbrook | Nathaniel Fairbrook
    </div>
  </section>
</main>
</body>
</html>
```